Oskrel - Business Card Design

Design a modern masculine business card for our business

Target Market(s)

Private Market

Industry/Entity Type

Construction

Contact Information for Business Card

Company Name - Name of Person - Address - email address - contact number

Font styles to use
Serif
Sans Serif

Colors
0094D4
00A9DD
6FCCEA
C7EBF8
E9F6FB
00AB8E
00BBA5
67D7C9
C6EFE9
E9F9F6
F0912C
F2A743
F7CA91
FBE8D2
FDF5EE

Requirements
Must have
• Use company logo provided
Nice to have
• Company Logo

```html
<!DOCTYPE html>
<html lang="en">
<head>
<meta charset="utf-8">
<title>Oskrel Construction – Business Card</title>
<link rel="stylesheet" href="https://fonts.googleapis.com/css2?family=Montserrat:wght@400;700;800&display=swap">
<style>
  :root {
    --page-bg: #2a2a2a;
    --card-bg: #1c1c1c;
    --brand-white: #ffffff;
    --accent-orange: #f0702c;
    --text-light: #e6e6e6;
  }
  * { margin: 0; padding: 0; box-sizing: border-box; }
  html, body {
    width: 1200px;
    height: 900px;
    overflow: hidden;
    background: var(--page-bg);
    font-family: "Montserrat", sans-serif;
  }
  .canvas {
    width: 1200px;
    height: 900px;
    display: flex;
    align-items: center;
    justify-content: center;
  }
  .business-card {
    position: relative;
    width: 1050px;
    height: 600px;
    background: var(--card-bg);
    box-shadow: 0 20px 50px rgba(0,0,0,0.5);
  }
  .brand {
    position: absolute;
    top: 70px;
    left: 270px;
    display: flex;
    align-items: flex-start;
    gap: 22px;
    color: var(--brand-white);
    font-weight: 800;
  }
  .brand-square {
    width: 54px;
    height: 54px;
    background: var(--brand-white);
    margin-top: 34px;
  }
  .brand-text { line-height: 1; text-align: right; }
  .brand-name {
    display: block;
    font-size: 150px;
    letter-spacing: 4px;
  }
  .brand-tagline {
    display: block;
    font-size: 34px;
    letter-spacing: 6px;
    margin-top: 10px;
  }
  .person {
    position: absolute;
    top: 380px;
    right: 600px;
    text-align: right;
    color: var(--text-light);
  }
  .person-name {
    font-size: 34px;
    font-weight: 700;
    color: var(--accent-orange);
  }
  .person-title {
    font-size: 20px;
    margin-top: 6px;
  }
  .person-address {
    font-size: 20px;
    line-height: 1.45;
    margin-top: 10px;
    font-style: normal;
  }
  .divider {
    position: absolute;
    top: 385px;
    left: 480px;
    width: 2px;
    height: 150px;
    background: var(--accent-orange);
  }
  .contact-list {
    position: absolute;
    top: 400px;
    left: 510px;
    list-style: none;
    color: var(--text-light);
    font-size: 22px;
  }
  .contact-item {
    display: flex;
    align-items: center;
    gap: 14px;
    margin-bottom: 14px;
  }
  .contact-icon { width: 20px; height: 20px; fill: var(--accent-orange); }
</style>
</head>
<body>
<div class="canvas">
  <section class="business-card">
    <div class="brand">
      <span class="brand-square"></span>
      <span class="brand-text">
        <span class="brand-name">OSKREL</span>
        <span class="brand-tagline">CONSTRUCTION, INC</span>
      </span>
    </div>

    <div class="person">
      <p class="person-name">Daniel Price</p>
      <p class="person-title">Owner</p>
      <address class="person-address">48 Harbor Lane, Suite 210<br>Millbrook, PA 17320</address>
    </div>

    <div class="divider"></div>

    <ul class="contact-list">
      <li class="contact-item">
        <svg class="contact-icon" viewBox="0 0 24 24" aria-hidden="true"><path d="M6.6 10.8a15.1 15.1 0 0 0 6.6 6.6l2.2-2.2a1 1 0 0 1 1-.25 11.4 11.4 0 0 0 3.6.57 1 1 0 0 1 1 1V20a1 1 0 0 1-1 1A17 17 0 0 1 3 4a1 1 0 0 1 1-1h3.5a1 1 0 0 1 1 1c0 1.25.2 2.45.57 3.57a1 1 0 0 1-.25 1z"/></svg>
        <span>555-204-7719</span>
      </li>
      <li class="contact-item">
        <svg class="contact-icon" viewBox="0 0 24 24" aria-hidden="true"><path d="M2 5h20v14H2z M2 5l10 8 10-8" fill="none" stroke="#f0702c" stroke-width="2"/></svg>
        <span>info@oskrelconstruction.com</span>
      </li>
      <li class="contact-item">
        <svg class="contact-icon" viewBox="0 0 24 24" aria-hidden="true"><circle cx="12" cy="12" r="9" fill="none" stroke="#f0702c" stroke-width="2"/><path d="M3 12h18M12 3c3 3.5 3 14.5 0 18M12 3c-3 3.5-3 14.5 0 18" fill="none" stroke="#f0702c" stroke-width="1.6"/></svg>
        <span>www.oskrelconstruction.com</span>
      </li>
    </ul>
  </section>
</div>
</body>
</html>
```